Business Cards for an 'affordable luxury' inner city home builder in Calgary.

We need a business card design that emulates the progressive, innovative, culture of our company and the modern style of our homes. Use our website www.velmarcrest-ab.com as a reference for the product we build.

Our company builds homes in the inner city space of Calgary, Alberta. We build affordable luxury.

Target Market(s)

Young professional Families

Contact Information for Business Card

Try to maintain consistency with the logo font and the card font.

Requirements
Must have
• The details must include: Name, education, title, phone number, website and email (Address is not as important)
• The design must be uniques (like our logo), elegant, sophisticated and modern.

```html
<!DOCTYPE html>
<html lang="en">
<head>
<meta charset="utf-8">
<title>Velmar Crest Homes Ltd — Business Card</title>
<link rel="stylesheet" href="https://fonts.googleapis.com/css2?family=Montserrat:wght@600&family=Open+Sans:wght@300;400&family=Lato:wght@300&display=swap">
<style>
  :root {
    --page: #ffffff;
    --ink: #262626;
    --frame-dark: #2b2b2b;
    --frame-light: #e8e8e8;
    --line-mid: #7a7a7a;
    --line-soft: #8e8e8e;
    --line-dim: #454545;
    --name-light: #dcdcdc;
    --tag-bg: #e4e4e4;
    --contact: #8a8a8a;
    --white: #ffffff;
  }
  html, body {
    margin: 0;
    width: 1200px;
    height: 1200px;
    overflow: hidden;
    background: var(--page);
  }
  .card {
    position: absolute;
    box-sizing: border-box;
    box-shadow: 2px 2px 3px rgba(0,0,0,0.35);
  }
  .card-front {
    left: 177.5px; top: 70px; width: 830px; height: 494px;
    background: var(--frame-dark);
  }
  .card-back {
    left: 167.5px; top: 629px; width: 830px; height: 494px;
    background: var(--frame-light);
  }
  .card-face {
    position: absolute;
    width: 781px; height: 446px;
    overflow: hidden;
  }
  .card-front .card-face { left: 24px; top: 20px; background: var(--white); }
  .card-back .card-face { left: 24px; top: 24px; background: var(--ink); }
  .decor-lines { position: absolute; left: 0; top: 0; width: 781px; height: 446px; }

  .brand { position: absolute; display: flex; align-items: flex-start; }
  .brand-square { flex: none; }
  .brand-name {
    font-family: 'Montserrat', sans-serif;
    font-weight: 600;
    text-transform: uppercase;
    margin: 0;
  }
  .card-front .brand { left: 240px; top: 164px; }
  .card-front .brand-square { width: 30px; height: 30px; background: var(--ink); margin: 12px 30px 0 0; }
  .card-front .brand-name { font-size: 30px; line-height: 31px; letter-spacing: 0.02em; color: var(--ink); }

  .website {
    position: absolute; left: 236px; top: 346px;
    display: flex; align-items: center; gap: 5px;
    font-family: 'Open Sans', sans-serif; font-size: 17.5px; color: #3a3a3a;
  }
  .website svg { width: 29px; height: 29px; }

  .person { position: absolute; left: 80px; top: 72px; }
  .person-name {
    margin: 0;
    font-family: 'Open Sans', sans-serif; font-weight: 300;
    font-size: 48px; line-height: 56px; letter-spacing: -0.02em;
    color: var(--name-light);
  }
  .person-title {
    display: inline-block; margin-top: 0;
    background: var(--tag-bg); color: var(--ink);
    font-family: 'Open Sans', sans-serif; font-size: 15.5px;
    letter-spacing: 0.42em; padding: 0 0 0 4px; line-height: 22px;
    width: 229px; box-sizing: border-box;
  }
  .card-back .brand { left: 512px; top: 84px; }
  .card-back .brand-square { width: 20px; height: 20px; background: var(--white); margin: 8px 14px 0 0; }
  .card-back .brand-name { font-size: 16.5px; line-height: 17.5px; letter-spacing: 0.02em; color: var(--white); }

  .contact-list {
    position: absolute; right: 57px; top: 267px;
    margin: 0; padding: 0; list-style: none; text-align: right;
    font-family: 'Lato', sans-serif; font-weight: 300;
    font-size: 16px; line-height: 32px; letter-spacing: 0.25em;
    color: var(--contact);
  }
</style>
</head>
<body>

<section class="card card-front">
  <div class="card-face">
    <svg class="decor-lines" viewBox="0 0 781 446" aria-hidden="true">
      <polyline points="621,446 621.5,147.5 781,145.5" fill="none" stroke="var(--line-soft)" stroke-width="4"/>
      <polyline points="690.5,446 690.5,66 781,67.5" fill="none" stroke="var(--line-mid)" stroke-width="4"/>
    </svg>
    <div class="brand">
      <span class="brand-square"></span>
      <h1 class="brand-name">Velmar<br>Crest<br>Homes Ltd</h1>
    </div>
    <div class="website">
      <svg viewBox="0 0 30 30" aria-hidden="true">
        <g fill="none" stroke="#3a3a3a" stroke-width="1.3">
          <circle cx="15" cy="15" r="13"/>
          <ellipse cx="15" cy="15" rx="6" ry="13"/>
          <line x1="15" y1="2" x2="15" y2="28"/>
          <line x1="2" y1="15" x2="28" y2="15"/>
          <path d="M4.5 8.5 H25.5 M4.5 21.5 H25.5"/>
        </g>
      </svg>
      <span>https://www.velmarcrest-ab.com</span>
    </div>
  </div>
</section>

<section class="card card-back">
  <div class="card-face">
    <svg class="decor-lines" viewBox="0 0 781 446" aria-hidden="true">
      <polyline points="0,65.5 89.5,64.5 89.5,446" fill="none" stroke="var(--line-dim)" stroke-width="2"/>
      <polyline points="0,143.5 89.5,144.5" fill="none" stroke="var(--line-dim)" stroke-width="2"/>
      <line x1="158" y1="145" x2="158" y2="446" stroke="var(--line-dim)" stroke-width="2"/>
    </svg>
    <div class="person">
      <h2 class="person-name">IVO LANE.R</h2>
      <span class="person-title">interior designer</span>
    </div>
    <div class="brand">
      <span class="brand-square"></span>
      <p class="brand-name">Velmar<br>Crest<br>Homes Ltd</p>
    </div>
    <ul class="contact-list">
      <li>403-555-0148</li>
      <li>projects@velmarcrest-ab.com</li>
      <li>https://www.velmarcrest-ab.com</li>
      <li>48 Larkin Ave NE Calgary, AB</li>
    </ul>
  </div>
</section>

</body>
</html>
```